Kestrova88 Business Card Redesign

I want to create a design for brand new business cards, I need something exceptional for clear plastic business card design. Please do not submit without it being on a clear design. Photos of the various logo versions attached.

```html
<!DOCTYPE html>
<html lang="en">
<head>
<meta charset="utf-8">
<title>Kestrova88 Business Card</title>
<link href="https://fonts.googleapis.com/css2?family=Poppins:wght@400;500;600&display=swap" rel="stylesheet">
<style>
  :root {
    --page-bg: #cbd5df;
    --card-clear: rgba(236, 241, 246, 0.78);
    --card-edge: rgba(255, 255, 255, 0.9);
    --navy: #28354f;
    --ink: #33415c;
    --gold: #b59c4e;
  }
  * { margin: 0; padding: 0; box-sizing: border-box; }
  html, body {
    width: 1200px;
    height: 900px;
    overflow: hidden;
    background: var(--page-bg);
    font-family: "Poppins", sans-serif;
  }
  .card {
    position: absolute;
    left: 100px;
    top: 165px;
    width: 1000px;
    height: 570px;
    background: linear-gradient(160deg, rgba(248, 251, 253, 0.85), var(--card-clear));
    border: 1px solid var(--card-edge);
    box-shadow: 0 18px 40px rgba(40, 55, 80, 0.18);
    overflow: hidden;
  }
  .card__panel {
    position: absolute;
    inset: 0;
    width: 100%;
    height: 100%;
  }
  .card__identity {
    position: absolute;
    left: 54px;
    top: 250px;
  }
  .brand-name {
    font-weight: 600;
    font-size: 52px;
    letter-spacing: 2px;
    color: var(--gold);
    line-height: 1;
  }
  .person {
    position: absolute;
    left: 54px;
    top: 348px;
    color: var(--ink);
  }
  .person__name {
    font-weight: 500;
    font-size: 34px;
    line-height: 1.1;
  }
  .person__role {
    font-size: 18px;
    letter-spacing: 1px;
    margin-top: 2px;
  }
  .contacts {
    position: absolute;
    left: 54px;
    top: 445px;
    list-style: none;
    color: var(--ink);
    font-size: 20px;
    letter-spacing: 0.5px;
  }
  .contacts__item {
    display: flex;
    align-items: center;
    gap: 20px;
    height: 28px;
  }
  .contacts__icon {
    width: 18px;
    height: 18px;
    fill: var(--ink);
    flex: none;
  }
</style>
</head>
<body>
  <div class="card">
    <svg class="card__panel" viewBox="0 0 1000 570" preserveAspectRatio="none" aria-hidden="true">
      <polygon points="820,0 1000,0 1000,570 530,570" fill="var(--navy)"/>
    </svg>

    <div class="card__identity">
      <p class="brand-name">Kestrova88</p>
    </div>

    <div class="person">
      <p class="person__name">Dana Whitcombe</p>
      <p class="person__role">Sales &amp; Estimating</p>
    </div>

    <ul class="contacts">
      <li class="contacts__item">
        <svg class="contacts__icon" viewBox="0 0 20 20"><path d="M3 7c0-2 3-4 7-4s7 2 7 4l-3 1-1-2H7L6 8 3 7zm2 2h10l1 8H4l1-8zm5 2a2 2 0 1 0 0 4 2 2 0 0 0 0-4z"/></svg>
        <span>(833) KSTR-088</span>
      </li>
      <li class="contacts__item">
        <svg class="contacts__icon" viewBox="0 0 20 20"><path d="M2 5h16v10H2z M2 5l8 6 8-6" stroke="var(--page-bg)" stroke-width="1"/></svg>
        <span>info@kestrova-88.com</span>
      </li>
      <li class="contacts__item">
        <svg class="contacts__icon" viewBox="0 0 20 20"><circle cx="10" cy="10" r="8"/><path d="M2 10h16M10 2c3 3 3 13 0 16M10 2c-3 3-3 13 0 16" stroke="var(--page-bg)" stroke-width="1" fill="none"/></svg>
        <span>www.kestrova-88.com</span>
      </li>
    </ul>
  </div>
</body>
</html>
```